Business Card & Stationary Design Project

We are looking for some creative direction for business cards and our stationary.

We are a global logistics firm that has recently changed its name to Marrick Global Logistics and we have a new website due out tomorrow (www.marrick.com.au).

The colours of the company are rich navy tones, I would like to have business cards that fit together to make one picture on the back (possibly an old map of the world??), and the front to be modern contemporary looking.

But I am open to suggestions, so just incorporate our new logo and get going!
Updates

Hi Everyone,

Thank you for all of your designs so far and the time you have put into it.

I have asked many of you for amendments to see if we can get a final product, so with this in mind I am extending the deadline by a few days.

Good luck and thank you once again.

Please message me direct if you need any clarification.

Kind Regards
Colin

Reason: As outlined the extra 3 days is for amendments and changes to the current submissions. Thanks Colin

Industry/Entity Type

Business

```html
<!DOCTYPE html>
<html lang="en">
<head>
<meta charset="utf-8">
<title>Marrick Global Logistics – Business Card</title>
<link rel="stylesheet" href="https://fonts.googleapis.com/css2?family=Open+Sans:wght@400;600&display=swap">
<style>
  :root {
    --page: #d9dadc;
    --card-light: #f4f5f6;
    --card-shade: #dfe1e4;
    --sky: #1ea7e1;
    --navy: #1c5eb1;
    --charcoal: #333436;
    --white: #ffffff;
  }
  * { box-sizing: border-box; margin: 0; padding: 0; }
  html, body { width: 1200px; height: 871px; overflow: hidden; }
  body {
    background: var(--page);
    font-family: "Open Sans", sans-serif;
    position: relative;
  }
  .card {
    position: absolute;
    left: 250px;
    width: 700px;
    height: 400px;
    background: linear-gradient(160deg, var(--card-light), var(--card-shade));
    box-shadow: 0 6px 18px rgba(0,0,0,.25);
    overflow: hidden;
  }
  .card--back { top: 22px; }
  .card--front { top: 449px; }

  /* back */
  .brand {
    position: absolute;
    left: 0; right: 0; top: 0; bottom: 0;
    display: flex; align-items: center; justify-content: center;
  }
  .brand__name {
    color: var(--charcoal);
    font-weight: 400;
    font-size: 32px;
    line-height: 1.2;
  }

  /* front */
  .bar {
    position: absolute;
    color: var(--white);
    display: flex; align-items: center;
    white-space: nowrap;
  }
  .bar--sky { background: var(--sky); }
  .bar--navy { background: var(--navy); }
  .bar--dark { background: var(--charcoal); }

  .name { font-size: 40px; padding-left: 14px; }
  .title { font-size: 34px; padding-left: 14px; }
  .address { font-size: 15px; padding-left: 60px; }
  .social { font-size: 19px; padding-left: 14px; gap: 14px; }
  .contact { font-size: 19px; justify-content: flex-end; padding-right: 14px; gap: 22px; }
  .contact span { min-width: 230px; text-align: center; }

  .dot { width: 22px; height: 22px; border-radius: 50%; background: var(--white); flex: none; }
  .icon { width: 22px; height: 22px; flex: none; }
  .mark-box {
    position: absolute; right: 20px; top: 8px;
    width: 32px; height: 32px; border: 3px solid var(--white);
  }
  .plus { position: absolute; right: 10px; top: -4px; font-size: 34px; }
</style>
</head>
<body>

<section class="card card--back" aria-label="Card back">
  <div class="brand">
    <p class="brand__name">Marrick Global Logistics</p>
  </div>
</section>

<section class="card card--front" aria-label="Card front">
  <div class="bar bar--sky" style="left:0;top:40px;width:300px;height:50px;"><span class="mark-box"></span></div>
  <div class="bar bar--dark name" style="left:305px;top:40px;width:395px;height:50px;">Arlen Pradhan</div>

  <div class="bar bar--navy" style="left:0;top:94px;width:210px;height:44px;"><span class="plus">+</span></div>
  <div class="bar bar--dark title" style="left:215px;top:94px;width:485px;height:44px;">General Manager</div>

  <div class="bar bar--dark address" style="left:0;top:142px;width:700px;height:38px;justify-content:space-between;padding-right:14px;">
    <span>2nd Floor, 14 Calloway St,&nbsp; P.O. Box 2290 East Perth WA 6004</span>
    <svg class="icon" viewBox="0 0 24 24"><path d="M12 3 2 12h3v9h5v-6h4v6h5v-9h3z" fill="#fff"/></svg>
  </div>

  <div class="bar bar--navy social" style="left:0;top:184px;width:345px;height:42px;"><span class="dot"></span>feed.marrick.com.au</div>
  <div class="bar bar--dark contact" style="left:350px;top:184px;width:350px;height:42px;">
    <span>+61 8 9225 4410</span>
    <svg class="icon" viewBox="0 0 24 24"><rect x="6" y="2" width="12" height="20" rx="2" fill="none" stroke="#fff" stroke-width="2"/><circle cx="12" cy="18" r="1.3" fill="#fff"/></svg>
  </div>

  <div class="bar bar--sky social" style="left:0;top:230px;width:300px;height:42px;"><span class="dot"></span>marrick.logistics</div>
  <div class="bar bar--dark contact" style="left:305px;top:230px;width:395px;height:42px;">
    <span>info@marrick.com.au</span>
    <svg class="icon" viewBox="0 0 24 24"><rect x="2" y="5" width="20" height="14" fill="#fff"/><path d="M2 5l10 8 10-8" fill="none" stroke="#333436" stroke-width="1.6"/></svg>
  </div>

  <div class="bar bar--sky social" style="left:0;top:276px;width:300px;height:42px;font-size:17px;"><span class="dot"></span>community.marrick.com.au</div>
  <div class="bar bar--dark contact" style="left:305px;top:276px;width:395px;height:42px;">
    <span>www.marrick.com.au</span>
    <svg class="icon" viewBox="0 0 24 24"><circle cx="12" cy="12" r="10" fill="none" stroke="#fff" stroke-width="2"/><path d="M2 12h20M12 2c4 4 4 16 0 20M12 2c-4 4-4 16 0 20" fill="none" stroke="#fff" stroke-width="1.5"/></svg>
  </div>
</section>

</body>
</html>
```